New packaging design for a current brand

We need a packing design (header & footer which wraps around the top and the bottom of the A5/4 card and sits in a hang/sell polybag ) for an existing brand name call Ned & Ivy.
Ned & Ivy sell 4 main crafting and scrapbooking products wholesale to large stores. These are as follows:
*A4 and A5 Corregated Card - 25 Colours in range - easy cut and peel and seal
*A4 and A5 Foam Card 25 colours in range - peel and stick
*A4 and A5 Glittersheets - 25 colours - peel and stick
*4 x Crafting shape punch - punches 6 different shapes at approx. 15mm/25mm/35mm/45mm radius
The above A4/A5 products are self - adhesive and easy cut so there is no need for glue. The punch can be used to cut out various different shapes to produce pictures, cards and used in scrapbooking etc.
We have uploaded the current packaging and some ideas of what we are looking for.

Reason: some of the design have asked for more time. we still have not seen what we are looking for peter

Pallox Market(s)

*We need a design producing for A4 Adults Range AND A5 kids range headers and footers.
We aim these products at both adults and children but the packaging needs to appeal to both
*A logo would need to be included on the header as well as the functionality eg, ‘PEEL & STICK’ or ‘EAY CUT’
*For the adults A4 packaging - we would like to show certain features of what you can actually do with the card/foam & glitter sheets on the packaging - these could be displayed in snapshots of crafting (see attached ‘Harbor Quest’ image +35 email as example)
*For children A5 packaging we would like to show certain features of what they can do with the card/foam sheets on the packaging these could be displayed through stick men and women using the card and cutouts for heads, shoes, clothes etc (see images attached ned & ivy kids email)
* All shapes can be easily cut out of the card/foam/glitter with the shape punch and easily stuck to be as creative as the child/adult would like. They can be used in scrapbooking, party invitations, card making, etc...
*Packaging needs to be modern, up to date, appealing, eye catching, exciting, innovative and preferably use the colour red/white/ black (in that order) and must appeal to both adults and children - but can have 2 different designs for this.

Industry/Entity Type

Call

Logo Text

Ned and Ivy

Font styles to use
Script
Other font styles liked:
• KBseriouslyIntoHer

Requirements
Must have
• We do have existing logo but want to change this. Keep the red.
• Ned & Ivy - need a fresh, new, clean , crisp, striking, standout, modern logo that will attract both adults and children alike. Needs to appeal to our wholesalers as well - eg, Vexco, Dorn P, Pallox as well as smaller retailers and stationary shops and newsagents and crafting stores.
• The logo needs to attract both adults & children but the packaging needs to target both adults & children but can be different styles with the same branding
Nice to have
• Likes:
• An up to date and modern font to appeal to adults and children
• Colours: Red/White/Back
• Stick boys/girls to appeal to children
• Fun packaging which will sell the product
• A way of showing how the product is used - see ideas in file 4 and 5

```html
<!DOCTYPE html>
<html lang="en">
<head>
<meta charset="utf-8">
<title>Ned &amp; Ivy – Peel &amp; Stick Header and Footer</title>
<link rel="stylesheet" href="https://fonts.googleapis.com/css2?family=Josefin+Sans:wght@400&family=Cabin+Condensed:wght@400;500&display=swap">
<style>
  :root {
    --brand-red: #ec1c24;
    --ink-black: #231f20;
    --paper-white: #ffffff;
    --sheet-rose: #d9505c;
    --sheet-rose-light: #e46d78;
    --sheet-rose-dark: #c7404d;
    --swatch-dark: #e8264a;
    --swatch-light: #f0634a;
    --label-text: #231f20;
  }
  html, body {
    margin: 0;
    padding: 0;
    width: 1200px;
    height: 852px;
    overflow: hidden;
    background: var(--paper-white);
  }
  .canvas {
    position: relative;
    width: 1200px;
    height: 852px;
  }
  .shapes {
    position: absolute;
    left: 0;
    top: 0;
  }
  .drop {
    filter: drop-shadow(2px 3px 3px rgba(0,0,0,0.28));
  }
  .brand-lockup {
    position: absolute;
    left: 130px;
    top: 352px;
    display: flex;
    align-items: center;
    gap: 16px;
  }
  .brand-lockup__square {
    width: 34px;
    height: 34px;
    background: var(--brand-red);
  }
  .brand-name {
    margin: 0;
    font-family: "Cabin Condensed", sans-serif;
    font-weight: 500;
    white-space: nowrap;
    line-height: 1;
  }
  .brand-name--standalone {
    font-size: 52px;
    color: var(--brand-red);
  }
  .brand-name--header {
    position: absolute;
    left: 612px;
    top: 166px;
    font-size: 56px;
    color: var(--paper-white);
  }
  .spec-label {
    position: absolute;
    left: 930px;
    top: 121px;
    width: 134px;
    font-family: "Josefin Sans", sans-serif;
  }
  .spec-label__thickness {
    margin: 16px 0 0;
    text-align: center;
    font-size: 17px;
    font-weight: 400;
    color: var(--label-text);
    letter-spacing: 0.5px;
  }
  .spec-label__swatch {
    margin: 0 auto;
    width: 97px;
    height: 21px;
    font-family: "Cabin Condensed", sans-serif;
    font-size: 9.5px;
    color: var(--paper-white);
    text-align: center;
    line-height: 21px;
  }
  .spec-label__swatch--dark { background: var(--swatch-dark); margin-top: 8px; }
  .spec-label__swatch--light { background: var(--swatch-light); margin-top: 7px; }
  .footer-copy {
    position: absolute;
    left: 603px;
    top: 635px;
    color: var(--paper-white);
    font-family: "Cabin Condensed", sans-serif;
  }
  .footer-copy__function {
    margin: 0;
    font-size: 60px;
    font-weight: 400;
    line-height: 1;
    letter-spacing: 0.5px;
  }
  .footer-copy__use {
    margin: 4px 0 0 2px;
    font-size: 19.5px;
    font-weight: 400;
    letter-spacing: 0.3px;
  }
</style>
</head>
<body>
<div class="canvas">
  <svg class="shapes" width="1200" height="852" viewBox="0 0 1200 852" xmlns="http://www.w3.org/2000/svg">
    <defs>
      <radialGradient id="sheetTone" cx="50%" cy="45%" r="70%">
        <stop offset="0%" stop-color="#e46d78"/>
        <stop offset="60%" stop-color="#d9505c"/>
        <stop offset="100%" stop-color="#c7404d"/>
      </radialGradient>
      <linearGradient id="craftTone" x1="0" y1="0" x2="1" y2="1">
        <stop offset="0%" stop-color="#3a2f2c"/>
        <stop offset="50%" stop-color="#d9a9ad"/>
        <stop offset="100%" stop-color="#5a4a44"/>
      </linearGradient>
    </defs>

    <g class="drop">
      <rect class="sheet" x="584" y="230" width="480" height="392" fill="url(#sheetTone)" role="img" aria-label="Rose glitter plush sheet texture"/>
    </g>

    <g class="drop">
      <rect class="header-band" x="584" y="121" width="346" height="141" fill="var(--brand-red)"/>
    </g>
    <g class="drop">
      <path class="spec-bubble" d="M930 121 H1064 V232 H1038 L990 277 L1010 232 H930 Z" fill="var(--paper-white)"/>
    </g>
    <rect class="hang-hole" x="787" y="137" width="81" height="20" rx="10" fill="var(--paper-white)"/>
    <circle cx="827" cy="137" r="10" fill="var(--paper-white)"/>

    <g class="drop">
      <path class="footer-band" d="M584 620 H1010 L990 575 L1040 620 H1064 V731 H584 Z" fill="var(--ink-black)"/>
    </g>
    <rect class="footer-snapshot" x="940" y="645" width="106" height="68" fill="url(#craftTone)" role="img" aria-label="Snapshot of hands peeling a glitter gift tag"/>
  </svg>

  <div class="brand-lockup">
    <span class="brand-lockup__square"></span>
    <p class="brand-name brand-name--standalone">Ned &amp; Ivy</p>
  </div>
  <p class="brand-name brand-name--header">Ned &amp; Ivy</p>

  <div class="spec-label">
    <p class="spec-label__thickness">2.3mm</p>
    <div class="spec-label__swatch spec-label__swatch--dark">dark orange plush</div>
    <div class="spec-label__swatch spec-label__swatch--light">orange plush</div>
  </div>

  <div class="footer-copy">
    <p class="footer-copy__function">PEEL &amp; STICK</p>
    <p class="footer-copy__use">ideal for invitations, cards &amp; scrapbooks</p>
  </div>
</div>
</body>
</html>
```